PELUNO soap beauty bar

I need a box designed to put a 4oz bar of soap inside. All sides of the box need design. A refreshingly fragrant blend of citrus and spicy notes, it is made with a blend of essential oils including ginger, mandarin, lemon and orange flowers

Target Market(s)

Homeless people

Requirements
Must have
• My company logo as pictured with text and design like a standard bar of soap. Weight 4oz, ingredients:
Olive oil, Coconut oil,Organic sustainable palm oil,Water,Lye,Shea butter, orange, ginger, mandarin, lemon essential oil. uploading pics for inspiration.
Nice to have
• The soap box measurements are Dimensions (L x W x H). 5.75 x 3.80 x 5.60 Inches ...

```html
<!DOCTYPE html>
<html lang="en">
<head>
<meta charset="utf-8">
<title>PELUNO soap beauty bar – box</title>
<link href="https://fonts.googleapis.com/css2?family=Montserrat:wght@400;600;800&family=Questrial&display=swap" rel="stylesheet">
<style>
  :root {
    --bg: #e5e6ea;
    --green: #3a9422;
    --green-dark: #2f7f2c;
    --pattern-light: #f4f7ee;
    --pattern-tone: #cfe0ad;
    --white: #ffffff;
    --ink: #2a2a2a;
    --accent-red: #d9232a;
  }
  html, body {
    margin: 0;
    padding: 0;
    width: 1200px;
    height: 890px;
    overflow: hidden;
    background: var(--bg);
  }
  .canvas {
    position: relative;
    width: 1200px;
    height: 890px;
  }
  .front-panel {
    position: absolute;
    left: 352px;
    top: 145px;
    width: 496px;
    height: 292px;
    overflow: hidden;
    background: var(--white);
  }
  .front-panel .pattern {
    position: absolute;
    inset: 0;
    background:
      radial-gradient(circle at 20% 25%, var(--pattern-tone) 0, transparent 28%),
      radial-gradient(circle at 60% 15%, var(--pattern-tone) 0, transparent 25%),
      radial-gradient(circle at 90% 70%, var(--pattern-tone) 0, transparent 30%),
      radial-gradient(circle at 15% 85%, var(--pattern-tone) 0, transparent 28%),
      radial-gradient(circle at 50% 95%, var(--pattern-tone) 0, transparent 22%),
      var(--pattern-light);
  }
  .brand-mark {
    position: absolute;
    left: 50%;
    top: 70px;
    width: 40px;
    height: 40px;
    margin-left: -20px;
    border-radius: 50%;
    background: var(--accent-red);
  }
  .brand-name {
    position: absolute;
    left: 0;
    right: 0;
    top: 138px;
    text-align: center;
    font-family: "Montserrat", sans-serif;
    font-weight: 800;
    font-size: 34px;
    letter-spacing: 1px;
    color: var(--green-dark);
  }
  .product-name {
    position: absolute;
    left: 0;
    right: 0;
    top: 198px;
    text-align: center;
    font-family: "Questrial", sans-serif;
    font-size: 21px;
    line-height: 26px;
    letter-spacing: 1px;
    color: var(--ink);
  }
  .net-weight {
    position: absolute;
    left: 0;
    right: 0;
    top: 260px;
    text-align: center;
    font-family: "Montserrat", sans-serif;
    font-weight: 600;
    font-size: 12px;
    letter-spacing: 1px;
    color: var(--green-dark);
  }
  .dieline {
    position: absolute;
    left: 345px;
    top: 501px;
    width: 453px;
    height: 340px;
  }
  .dieline .label-heading { font-family: "Montserrat", sans-serif; font-weight: 600; font-size: 12px; fill: var(--white); }
  .dieline .label-copy { font-family: "Montserrat", sans-serif; font-weight: 400; font-size: 9.5px; fill: var(--white); }
  .dieline .side-name { font-family: "Montserrat", sans-serif; font-weight: 800; font-size: 44px; fill: var(--green); }
  .dieline .front-name { font-family: "Montserrat", sans-serif; font-weight: 800; font-size: 30px; fill: var(--green); }
  .dieline .front-product { font-family: "Questrial", sans-serif; font-size: 19px; fill: var(--ink); }
</style>
</head>
<body>
<main class="canvas">

  <section class="front-panel">
    <div class="pattern" role="img" aria-label="Soft green swirl pattern background"></div>
    <div class="brand-mark"></div>
    <div class="brand-name">PELUNO</div>
    <div class="product-name">Soap beauty bar<br>citrus &amp; ginger</div>
    <div class="net-weight">NET WT. 4 OZ (113 g)</div>
  </section>

  <svg class="dieline" viewBox="640 930 840 630" xmlns="http://www.w3.org/2000/svg">
    <defs>
      <radialGradient id="swirl-tone" cx="50%" cy="50%" r="70%">
        <stop offset="0" stop-color="#e8f0d8"/>
        <stop offset="1" stop-color="#cfe0ad"/>
      </radialGradient>
    </defs>

    <!-- back panel with glue flaps -->
    <polygon fill="var(--green)"
      points="750,940 890,940 890,1000 935,1045 935,1435 890,1480 890,1548 748,1548 748,1500 705,1480 705,1460 650,1410 650,1080 700,1060 705,1025 748,1020"/>
    <g transform="translate(728 1405) rotate(-90)">
      <text class="label-heading" x="0" y="0">PELUNO SOAP BEAUTY BAR</text>
      <text class="label-copy" x="0" y="16">A refreshingly fragrant blend of citrus and spicy notes,</text>
      <text class="label-copy" x="0" y="28">made with ginger, mandarin, lemon and orange flower oils.</text>
      <text class="label-heading" x="0" y="54">DIRECTIONS</text>
      <text class="label-copy" x="0" y="70">Wet bar and hands, work into a rich lather, rinse well.</text>
      <text class="label-copy" x="0" y="82">Keep the bar dry between uses so it lasts longer.</text>
      <text class="label-heading" x="0" y="108">INGREDIENTS</text>
      <text class="label-copy" x="0" y="124">Olive oil, coconut oil, organic sustainable palm oil,</text>
      <text class="label-copy" x="0" y="136">water, lye, shea butter, orange, ginger, mandarin</text>
      <text class="label-copy" x="0" y="148">and lemon essential oils.</text>
      <text class="label-heading" x="0" y="176">NET WT. 4 OZ (113 g)</text>
    </g>

    <!-- left side panel -->
    <polygon fill="var(--green)" points="960,965 1062,965 1085,1035 1085,1065 940,1065 940,1035"/>
    <rect x="940" y="1065" width="145" height="365" fill="var(--white)"/>
    <polygon fill="var(--green)" points="940,1430 1085,1430 1085,1460 1065,1525 960,1525 940,1460"/>
    <text class="side-name" transform="translate(1027 1340) rotate(-90)">PELUNO</text>

    <!-- front panel -->
    <polygon fill="var(--white)" points="1110,940 1285,940 1285,965 1300,975 1325,975 1325,1065 1088,1065 1088,975 1100,965"/>
    <rect x="1088" y="1065" width="237" height="365" fill="url(#swirl-tone)" role="img" aria-label="Soft green swirl pattern"/>
    <rect x="1095" y="1430" width="218" height="120" fill="var(--white)"/>
    <circle cx="1160" cy="1245" r="22" fill="var(--accent-red)"/>
    <text class="front-name" transform="translate(1225 1315) rotate(-90)">PELUNO</text>
    <text class="front-product" transform="translate(1265 1330) rotate(-90)">Soap beauty bar</text>
    <text class="front-product" transform="translate(1290 1330) rotate(-90)">citrus &amp; ginger · 4 oz</text>

    <!-- right side panel -->
    <polygon fill="var(--green)" points="1348,965 1470,965 1470,1065 1325,1065 1325,1035"/>
    <rect x="1325" y="1065" width="145" height="365" fill="var(--white)"/>
    <polygon fill="var(--green)" points="1325,1430 1470,1430 1470,1525 1352,1525 1325,1460"/>
    <circle cx="1395" cy="1245" r="20" fill="var(--accent-red)"/>
  </svg>

</main>
</body>
</html>
```